Lowmoor Guild - Crossroads CD Cover

To prepare a CD Cover for the single "Crossroads" by Lowmoor Guild.
You can hear the single here:
http://lowmoorguild.com/listen/

The LMG logo and backdrop are also provided if you want to incorporate them into the CD cover design, though that isn't mandatory.

Song is about deciding on taking on a serious relationship, and leaving the single life behind.

Target Market(s)

Music listeners, 18-50 yrs old, into retro 80s, Marigolds/Dune Riders

Industry/Entity Type

Music Download

Requirements
Must have
• LMG logo
• Crossroads title
Nice to have
• Use of backdrop, or facimile
Should not have
• Too obvious on the term Crossroads

```html
<!DOCTYPE html>
<html lang="en">
<head>
<meta charset="utf-8">
<title>Lowmoor Guild – Crossroads</title>
<link href="https://fonts.googleapis.com/css2?family=Big+Shoulders+Display:wght@400&family=Caveat+Brush&display=swap" rel="stylesheet">
<style>
  :root {
    --stage: #1d202b;
    --sky-deep: #08090e;
    --sky-mid: #10132a;
    --sky-glow: #1c2260;
    --ink: #ffffff;
  }
  html, body {
    margin: 0;
    padding: 0;
    overflow: hidden;
  }
  body {
    width: 1200px;
    height: 1114px;
    background: var(--stage);
    position: relative;
  }
  .cover {
    position: absolute;
    left: 134px;
    top: 96px;
    width: 936px;
    height: 900px;
    overflow: hidden;
  }
  .cover__backdrop {
    position: absolute;
    inset: 0;
    background:
      radial-gradient(ellipse 45% 30% at 18% 62%, var(--sky-glow) 0%, transparent 70%),
      radial-gradient(ellipse 40% 25% at 75% 22%, var(--sky-glow) 0%, transparent 70%),
      radial-gradient(ellipse 70% 70% at 50% 50%, var(--sky-mid) 0%, var(--sky-deep) 100%);
  }
  .cover__type {
    position: absolute;
    inset: 0;
  }
  .band-name {
    font-family: "Big Shoulders Display", "Arial Narrow", sans-serif;
    font-weight: 400;
    fill: var(--ink);
  }
  .single-title {
    font-family: "Caveat Brush", cursive;
    fill: var(--ink);
  }
</style>
</head>
<body>
  <section class="cover">
    <div class="cover__backdrop" role="img" aria-label="Night sky scattered with stars and softly coloured floating bubbles"></div>
    <svg class="cover__type" width="936" height="900" viewBox="0 0 936 900" aria-label="Lowmoor Guild – Crossroads">
      <text class="band-name" x="330" y="328" font-size="210" textLength="288" lengthAdjust="spacingAndGlyphs">LOW</text>
      <text class="band-name" x="330" y="496" font-size="190" textLength="288" lengthAdjust="spacingAndGlyphs">MOOR</text>
      <text class="band-name" x="330" y="616" font-size="125" textLength="288" lengthAdjust="spacingAndGlyphs">GUILD</text>
      <text class="single-title" x="334" y="704" font-size="72" textLength="280" lengthAdjust="spacingAndGlyphs">Crossroads</text>
    </svg>
  </section>
</body>
</html>
```